Create look and feel for existing Web Page

Update Web Page

We have a website at http://www.usekivra.com/index-web.html. It is a single page html site, with a custom signup form. We also have a quill bay plugin at the bottom of the page. We'd like to redesign the look and feel of the entire site. We sell software to eye doctors. Also called optometrists, our software tool makes it easy for doctors to manage patients, bill, and document patient encounters. I have included our logos below.

We are looking for a new design preferably in HTML 5, CSS etc. The fields on the form on this page: http://www.usekivra.com/index-web.html

You can get screen shots of our software application at this site: http://staging.usekivra.com
username: test@samplevora.com
password: password

```html
<!DOCTYPE html>
<html lang="en">
<head>
<meta charset="utf-8">
<title>Orvane — The Practice Operating System</title>
<link rel="stylesheet" href="https://fonts.googleapis.com/css2?family=Montserrat:wght@300;400;500;600;700;800&display=swap">
<style>
:root{
  --orange:#ff8716;
  --orange-soft:#ffc48e;
  --navy:#3b3f4d;
  --light:#f2f2f3;
  --text:#4a4a4a;
  --muted:#6d6d6d;
  --white:#ffffff;
  --footer:#2a2b2f;
}
*{box-sizing:border-box;margin:0;padding:0}
html,body{width:1200px;height:3516px;overflow:hidden}
body{font-family:"Montserrat",sans-serif;color:var(--text);background:var(--white);position:relative}
.abs{position:absolute}

/* hero */
.hero{left:0;top:0;width:1200px;height:600px;background:linear-gradient(120deg,#6b5a4c 0%,#a08a76 35%,#7b4b56 60%,#4a3a35 100%)}
.hero::after{content:"";position:absolute;inset:0;background:rgba(30,25,25,.35)}
.nav{left:171px;top:20px;width:858px;height:36px;z-index:2;display:flex;align-items:center;justify-content:space-between}
.brand{font-size:28px;font-weight:500;color:var(--white);letter-spacing:.5px}
.nav-links{display:flex;gap:36px;list-style:none}
.nav-links li{font-size:12px;color:var(--white);letter-spacing:.4px}
.hero-title{left:0;top:252px;width:1200px;text-align:center;z-index:2;color:var(--white);font-size:33px;font-weight:700;letter-spacing:1px}
.hero-sub{left:0;top:310px;width:1200px;z-index:2;display:flex;justify-content:center;align-items:center;gap:24px;color:var(--white);font-size:19px;font-weight:600;letter-spacing:.5px}
.dot{width:12px;height:12px;border-radius:50%;background:var(--orange)}
.hero-btn{left:471px;top:381px;width:259px;height:44px;z-index:2;background:var(--white);color:#222;font-size:11px;font-weight:500;display:flex;align-items:center;justify-content:center;letter-spacing:.3px}

/* feature cards */
.card{top:490px;width:269px;height:221px;padding:28px 15px;color:var(--white);z-index:3}
.card.orange{background:var(--orange)}
.card.navy{background:var(--navy)}
.card h3{font-size:19px;font-weight:800;line-height:25px;letter-spacing:.5px;color:#222;margin-bottom:20px}
.card.navy h3{color:var(--white)}
.card p{font-size:11px;line-height:16.5px}
.card.orange p{color:#3a2000}

/* section headings */
.heading{font-size:31px;font-weight:300;color:#222;letter-spacing:.5px}
.heading b{color:var(--orange);font-weight:700}
.rule{width:52px;height:3px;background:var(--orange)}
.lead{font-size:14px;line-height:20px;color:var(--text)}
.dark-btn{background:var(--navy);color:var(--white);font-size:11px;font-weight:600;display:flex;align-items:center;justify-content:center;letter-spacing:.3px}

/* devices */
.devices{left:614px;top:782px;width:410px;height:262px;background:linear-gradient(135deg,#e9ebee,#c9ccd2 55%,#f4f5f7);border-radius:6px}

/* tasks grid */
.tasks{left:173px;top:1302px;width:852px;height:459px;display:grid;grid-template-columns:repeat(3,284px);grid-template-rows:repeat(2,229.5px)}
.task{text-align:center;padding:36px 24px 0}
.task svg{width:52px;height:52px;display:block;margin:0 auto 16px}
.task h4{font-size:19px;font-weight:700;margin-bottom:16px;letter-spacing:.4px}
.task p{font-size:12px;line-height:19px}
.task.orange{background:var(--orange);color:var(--white)}
.task.orange h4{color:var(--white)}
.task.navy{background:var(--navy);color:var(--white)}
.task.light{background:var(--light);color:var(--muted)}
.task.light h4{color:#222}

/* pricing */
.plan{width:270px;height:270px;background:var(--light);border:1px solid #e3e3e3}
.plan-top{height:121px;background:var(--navy);text-align:center;color:var(--white);padding-top:26px}
.price{font-size:46px;font-weight:400;color:var(--orange);line-height:54px}
.price small{font-size:20px;color:var(--white);font-weight:400}
.per{font-size:13px;font-weight:500;margin-top:6px}
.plan-body{text-align:center;padding:14px 14px 0}
.plan-name{font-size:23px;font-weight:400;color:#222;padding-bottom:12px;margin:0 10px 14px;border-bottom:2px dotted #999}
.plan-body p{font-size:11px;line-height:19px;color:var(--muted)}

/* cta */
.cta{left:0;top:2622px;width:1200px;height:134px;background:linear-gradient(90deg,var(--orange) 0%,#ffa14c 55%,var(--orange-soft) 100%)}
.cta-text{left:176px;top:2668px;font-size:26px;color:var(--white);font-weight:400;letter-spacing:1px}
.cta-btn{left:837px;top:2669px;width:184px;height:42px}

/* signup */
.photo{left:602px;top:2756px;width:598px;height:693px;background:linear-gradient(160deg,#b9b3a8 0%,#8f8e8a 40%,#3d4556 75%,#2c2f38 100%)}
.form{left:172px;top:3041px;width:379px}
.field{height:47px;background:var(--light);border:1px solid #dcdcdc;margin-bottom:11.7px;display:flex;align-items:center;justify-content:space-between;font-size:12px;color:#aaa}
.field span{padding-left:14px}
.field i{width:46px;height:100%;border-left:1px solid #dcdcdc;display:flex;align-items:center;justify-content:center}
.field svg{width:13px;height:13px;fill:#999}
.submit{width:379px;height:48px;background:var(--navy);color:var(--orange);font-size:12px;font-weight:600;display:flex;align-items:center;justify-content:center;margin-top:1px}

/* footer */
.footer{left:0;top:3449px;width:1200px;height:67px;background:var(--footer)}
.footer-brand{left:171px;top:3465px;font-size:28px;font-weight:500;color:var(--orange)}
.copyright{right:173px;top:3477px;font-size:11px;color:#8a8a8a}
</style>
</head>
<body>

<div class="abs hero" role="img" aria-label="Photo of a smiling woman holding a coffee cup at a café table"></div>
<nav class="abs nav">
  <div class="brand">orvane</div>
  <ul class="nav-links"><li>HOME</li><li>PRODUCTS</li><li>PRICING</li><li>SIGN UP</li></ul>
</nav>
<h1 class="abs hero-title">MEET ORVANE, THE PRACTICE OPERATING SYSTEM</h1>
<div class="abs hero-sub"><span>SIMPLE</span><i class="dot"></i><span>FULLY AUTOMATED</span><i class="dot"></i><span>PROFITABLE</span></div>
<div class="abs hero-btn">GET THE CHARTING TOOL FOR FREE</div>

<div class="abs card orange" style="left:172px">
  <h3>Designed For Lease Doctors</h3>
  <p>Lease doctors were frustrated with the administration associated with running a lease practice so instead of complaining they created a system to do it for them.</p>
</div>
<div class="abs card navy" style="left:465px">
  <h3>Starting @<br>$49 / Month</h3>
  <p>You start with charting at $49/mon and then add features as you need them. What other software allows you to only pay for what you want?</p>
</div>
<div class="abs card orange" style="left:758px">
  <h3>Just You &amp; Orvane Can Run Your Lease Practise</h3>
  <p>No really, you need to check Orvane out. If you want, your lease can be completely automated. No more late nights and HR frustrations.</p>
</div>

<!-- about -->
<h2 class="abs heading" style="left:171px;top:815px">About <b>Orvane</b></h2>
<div class="abs rule" style="left:172px;top:862px"></div>
<p class="abs lead" style="left:171px;top:898px;width:400px">Orvane is your office operating system. Automate your painful tasks, keep track of your books, and live a little. Start with a FREE charting tool and add more products as you grow.</p>
<div class="abs dark-btn" style="left:172px;top:1007px;width:242px;height:33px">GET THE CHARTING TOOL FOR FREE</div>
<div class="abs devices" role="img" aria-label="Orvane dashboard shown on a desktop monitor, tablet and phone"></div>

<!-- tasks -->
<h2 class="abs heading" style="left:171px;top:1145px">AI to Automate <b>Optometry Office Tasks</b></h2>
<div class="abs rule" style="left:172px;top:1200px"></div>
<p class="abs lead" style="left:171px;top:1228px;width:650px">Orvane uses AI, automation, robots, and other cool technology to streamline office work so you can do things you love</p>

<div class="abs tasks">
  <div class="task orange">
    <svg viewBox="0 0 52 52" fill="none" stroke="#222" stroke-width="2"><rect x="8" y="10" width="34" height="32" rx="2"/><path d="M8 18h34M14 6v8M22 6v8M30 6v8M38 6v8M42 36l4 6H12"/><g fill="#222" stroke="none"><rect x="13" y="23" width="4" height="3"/><rect x="20" y="23" width="4" height="3"/><rect x="27" y="23" width="4" height="3"/><rect x="34" y="23" width="4" height="3"/><rect x="13" y="30" width="4" height="3"/><rect x="20" y="30" width="4" height="3"/><rect x="27" y="30" width="4" height="3"/><rect x="34" y="30" width="4" height="3"/></g></svg>
    <h4>Schedule</h4>
    <p>Meet your patients where they are, 24 hours 7 days a week with the online scheduler.</p>
  </div>
  <div class="task navy">
    <svg viewBox="0 0 52 52" fill="none" stroke="#fff" stroke-width="2"><rect x="10" y="9" width="28" height="34" rx="2"/><path d="M15 6v6M21 6v6M27 6v6M33 6v6M15 20h16M15 26h12M15 32h8M44 18L30 34l-3 6 6-3 14-16z"/></svg>
    <h4>Intake</h4>
    <p>Never print out another paper form. Your patients are now able to fill out and sign forms online.</p>
  </div>
  <div class="task light">
    <svg viewBox="0 0 52 52" fill="none" stroke="#ff8716" stroke-width="2"><path d="M24 8a18 18 0 1 0 18 20H24z"/><path d="M29 4a18 18 0 0 1 17 17H29z"/></svg>
    <h4>Chart</h4>
    <p>Start charting all patient findings for FREE. With features like auto population it flies on your mobile phone.</p>
  </div>
  <div class="task navy">
    <svg viewBox="0 0 52 52" fill="none" stroke="#fff" stroke-width="2"><path d="M10 14h24v30H14a4 4 0 0 1-4-4zM14 44a4 4 0 0 0 4-4V38H6v2a4 4 0 0 0 4 4M16 22h12M16 28h12M16 34h8"/><circle cx="38" cy="12" r="8"/><path d="M38 7v10M35.5 9.5h4a1.5 1.5 0 0 1 0 3h-3a1.5 1.5 0 0 0 0 3h4"/></svg>
    <h4>Bill</h4>
    <p>Don't waste your precious time or pay someone to bill insurance, let a bot do it for you.</p>
  </div>
  <div class="task light">
    <svg viewBox="0 0 52 52" fill="none" stroke="#ff8716" stroke-width="2"><rect x="6" y="8" width="40" height="28" rx="1"/><path d="M20 36v6h12v-6M14 44h24M12 14h14v10H12zM30 14h10M30 19h10M30 24h6M12 29h28"/></svg>
    <h4>Eligible</h4>
    <p>Don't call or login into every insurance website to get patient eligibility and copays. Our bots do that too.</p>
  </div>
  <div class="task orange">
    <svg viewBox="0 0 52 52" fill="none" stroke="#222" stroke-width="2"><path d="M14 14h30a4 4 0 0 1 4 4v14a4 4 0 0 1-4 4H26l-8 8v-8h-4a4 4 0 0 1-4-4V18a4 4 0 0 1 4-4zM18 22h22M18 27h22M18 32h14"/><path d="M6 6h6v6l-3 4M14 6h6v6l-3 4" fill="#222"/></svg>
    <h4>Review</h4>
    <p>Grow your patient base and improve your Seekra results with the review solution.</p>
  </div>
</div>

<!-- pricing -->
<h2 class="abs heading" style="left:0;top:1863px;width:1200px;text-align:center">Orvane <b>Pricing</b></h2>
<div class="abs rule" style="left:574px;top:1913px"></div>

<div class="abs plan" style="left:172px;top:1966px"><div class="plan-top"><div class="price">$0<small>/month</small></div><div class="per">No strings attached</div></div><div class="plan-body"><div class="plan-name">Free</div><p>Chart patient findings for FREE. Unlimited users, doctors, and location.</p></div></div>
<div class="abs plan" style="left:465px;top:1966px"><div class="plan-top"><div class="price">$99<small>/month</small></div><div class="per">Per location</div></div><div class="plan-body"><div class="plan-name">Pick 1 Add-On</div><p>Choose between schedule, intake, bill, eligible, or review.</p></div></div>
<div class="abs plan" style="left:758px;top:1966px"><div class="plan-top"><div class="price">$189<small>/month</small></div><div class="per">Per location</div></div><div class="plan-body"><div class="plan-name">Pick 2 Add-Ons</div><p>Choose any two features between schedule, intake, bill, eligible, and/or review.</p></div></div>
<div class="abs plan" style="left:172px;top:2262px"><div class="plan-top"><div class="price">$279<small>/month</small></div><div class="per">Per location</div></div><div class="plan-body"><div class="plan-name">Pick 3 Add-Ons</div><p>Choose any three features between schedule, intake, bill, eligible, and/or review.</p></div></div>
<div class="abs plan" style="left:465px;top:2262px"><div class="plan-top"><div class="price">$369<small>/month</small></div><div class="per">Per location</div></div><div class="plan-body"><div class="plan-name">Pick 4 Add-Ons</div><p>Choose any four features between schedule, intake, bill, eligible, and/or review.</p></div></div>
<div class="abs plan" style="left:758px;top:2262px"><div class="plan-top"><div class="price">$459<small>/month</small></div><div class="per">Per location</div></div><div class="plan-body"><div class="plan-name">Pick All Add-Ons</div><p>Get all five features: schedule, intake, bill, eligible, and/or review.</p></div></div>

<!-- cta -->
<div class="abs cta"></div>
<p class="abs cta-text">Now spend time outside the office!</p>
<div class="abs dark-btn cta-btn">JOIN THE CLUB</div>

<!-- signup -->
<h2 class="abs heading" style="left:171px;top:2826px;line-height:44px">Get Started With A<br><b>Free Charting Tool</b></h2>
<div class="abs rule" style="left:172px;top:2922px"></div>
<p class="abs lead" style="left:171px;top:2963px;width:410px;line-height:22px">Become part of a club that wants to change the way we practice, so we can have a life outside of the office.</p>

<form class="abs form">
  <div class="field"><span>Name...</span><i><svg viewBox="0 0 16 16"><circle cx="8" cy="5" r="3.5"/><path d="M1 16c0-4 3-6 7-6s7 2 7 6z"/></svg></i></div>
  <div class="field"><span>Email...</span><i><svg viewBox="0 0 16 16"><path d="M0 3h16v2L8 10 0 5zM0 7l8 5 8-5v7H0z"/></svg></i></div>
  <div class="field"><span>Cell Phone...</span><i><svg viewBox="0 0 16 16"><path d="M3 1l3 3-2 2c1 2 3 4 6 6l2-2 3 3-2 2C7 15 1 9 1 3z"/></svg></i></div>
  <div class="field"><span>Office Name...</span><i><svg viewBox="0 0 16 16"><path d="M11 1l4 4-9 9H2v-4zM1 15h4"/></svg></i></div>
  <div class="field"><span>NPI...</span><i><svg viewBox="0 0 16 16"><path d="M7 1h2v5.3l4.6-2.6 1 1.7L10 8l4.6 2.6-1 1.7L9 9.7V15H7V9.7l-4.6 2.6-1-1.7L6 8 1.4 5.4l1-1.7L7 6.3z"/></svg></i></div>
  <div class="submit">GET THE FREE CHARTING TOOL</div>
</form>
<div class="abs photo" role="img" aria-label="Photo of a smiling businessman in a suit holding a laptop outdoors"></div>

<!-- footer -->
<div class="abs footer"></div>
<div class="abs footer-brand">orvane</div>
<p class="abs copyright">©Copyright information here</p>

</body>
</html>
```